Healthcare Technology Company Business Card Design

Hi,

We require a new business card design thats catchy and professional.
Our target audience is healthcare professionals. See supplied artwork for our logo.

If you think its achievable please try add the tag line, not necessary however.
"Developing technologies to improve patient care and release operation benefits"

We'll require the following information on the card. No need to have the subject titles but i've referenced them for your convenience.

Personal Details
Paul Dwyer
Position: Director
Phone Number - 03 9472 5836
Mobile Number - 0438 275 904
Email: firstname.lastname@mediqbay.com.au

Company Details
Suite 31, 286 Keldon Street
Port Melbourne, Victoria
Fax: 03 8241 3975
mediqbay.com.au

Prefer a thinner design than the normal stock standard business card dimensions.
Please ensure there is adequate bleed.

Target Market(s)

Healthcare Professionals

Industry/Entity Type

Healthcare

Font styles to use
Sans Serif

Requirements
Must have
• Clean, Sharp Looks
Should not have
• Any healthcare symbols

```html
<!DOCTYPE html>
<html lang="en">
<head>
<meta charset="utf-8">
<title>Mediqbay – Business Card</title>
<link rel="stylesheet" href="https://fonts.googleapis.com/css2?family=Arimo:wght@400&display=swap">
<style>
  :root {
    --card-bg: #0e1012;
    --name-blue: #8fd6f2;
    --text-light: #d2d4d6;
    --text-muted: #8c8f93;
    --brand-blue: #2b6cae;
    --brand-orange: #f28a1a;
  }
  * { margin: 0; padding: 0; box-sizing: border-box; }
  html, body {
    width: 1200px;
    height: 653px;
    overflow: hidden;
    background: var(--card-bg);
  }
  .card {
    position: relative;
    width: 1200px;
    height: 653px;
    background: var(--card-bg);
    font-family: "Arimo", Arial, sans-serif;
    color: var(--text-light);
    overflow: hidden;
  }
  .contact {
    position: absolute;
    left: 66px;
    top: 128px;
  }
  .contact__name {
    font-size: 28px;
    font-weight: 400;
    color: var(--name-blue);
    letter-spacing: 0.5px;
    line-height: 34px;
  }
  .contact__role {
    font-size: 23px;
    line-height: 28px;
    color: var(--text-light);
  }
  .contact__group {
    margin-top: 28px;
    font-size: 22px;
    line-height: 27px;
  }
  .contact__group--tight { margin-top: 27px; }
  .brand {
    position: absolute;
    left: 789px;
    top: 132px;
    display: flex;
    align-items: center;
    gap: 16px;
  }
  .brand__mark {
    width: 46px;
    height: 46px;
    background: var(--brand-orange);
  }
  .brand__name {
    font-size: 54px;
    line-height: 60px;
    color: var(--brand-blue);
    letter-spacing: -0.5px;
  }
  .tagline {
    position: absolute;
    left: 894px;
    top: 228px;
    font-size: 15px;
    line-height: 21px;
    color: var(--text-muted);
    letter-spacing: 0.6px;
  }
  .footer-band {
    position: absolute;
    left: 0;
    bottom: 0;
    width: 1200px;
    height: 37px;
    display: block;
  }
</style>
</head>
<body>
  <div class="card">
    <div class="contact">
      <div class="contact__name">PAUL DWYER</div>
      <div class="contact__role">Director</div>

      <div class="contact__group">
        <div>Ph - 03 9472 5836</div>
        <div>Mb - 0438 275 904</div>
      </div>

      <div class="contact__group">
        <div>Fax: 03 8241 3975</div>
      </div>

      <div class="contact__group">
        <div>Website: mediqbay.com.au</div>
        <div>Email: firstname.lastname@mediqbay.com.au</div>
      </div>

      <div class="contact__group contact__group--tight">
        <div>Suite 31, 286 Keldon Street Port Melbourne, Victoria</div>
      </div>
    </div>

    <div class="brand">
      <span class="brand__mark"></span>
      <span class="brand__name">Mediqbay</span>
    </div>

    <div class="tagline">
      Developing technologies to<br>
      improve patient care and<br>
      release operation benefits
    </div>

    <svg class="footer-band" viewBox="0 0 1200 37" preserveAspectRatio="none" aria-hidden="true">
      <polygon points="0,0 735,0 720,37 0,37" fill="var(--brand-blue)"/>
      <polygon points="775,0 1200,0 1200,37 760,37" fill="var(--brand-orange)"/>
    </svg>
  </div>
</body>
</html>
```